LunaGowns.com Banner AD

We are looking for some talented creators to create for us a banner ad for our online clothing store that specializes in dresses. We are looking for a fresh, clean, and sleek KORA, P&Q, and Glint appeal- clean, modern and sophisticated.

We would like for the final project to appear professionally done, we've had projects completed by several talent out there that did not capture our image, and let's just say it was too cluttered and appeared as if a high school editor had completed it.

I have attached a few files for you to reference, I have File 1, 2, 3, 8 and the P&Q photos as examples of what we DO like.

I have attached File 5, which is the work of one the designers that was working on this project. Although it is very simple and gets the point across, it doesn't come across like a magazine editorial.

I have attached File 6, that is the main photo we wish to use for our banner.

I have attached File 7, which is what a creator had done for us via Brevora.com, that is a good example of what we do NOT want.

That is about sums it up! I hope the examples are useful tools for you!

Hi Designers!

Thank you so much for your submissions! I enjoy viewing each and every one of them! Please view my update on what I am looking for, I have made some adjustments and have added a few more examples to reference, I have made my direction a bit more clearer. Because it seems some designers are not quite understanding my direction. I know you all have amazing talent and I am hoping to see something I am looking for and I love soon! If you have any other questions, please don't hesitate to ask! 

Target Market(s)

Our company targets women of all ages, we carry dresses that cater to every occasion, whether its an older woman looking for a dress to attend a wedding or a teenager looking for a prom dress. We want our front page banner to appear fresh, clean, with a feminine touch, we want to stray from tacky (gradients, etc..) and keep it classy all while maintaining that magazine editorial element, we want to be more fashion focused, like Glint. We want this project to appear professionally done. Our desired concept is something out of a magazine editorial, not too much going on, while shifting focus more on the dress itself than a design element like flowers or spring backgrounds.

Industry/Entity Type

High School

Requirements
Must have
• We want a glint fashion appeal, magazine editorial type of look. The phrases below should be included"

"New Season New Sexy Dresses"

"Free U.S shipping on orders $75+"
"Shop our sales up to 60% off"

All of the other phrases do not need to be included. Also, Do not include the parenthesis.
Should not have
• Only include the photo I've attached that appears solo. Please do not include the other 3 dresses that is displayed in a banner that was created for us by another designer. (that is provided as an example only)

```html
<!DOCTYPE html>
<html lang="en">
<head>
<meta charset="utf-8">
<title>LunaGowns.com – New Season Banner</title>
<link rel="stylesheet" href="https://fonts.googleapis.com/css2?family=Jost:wght@400;500&family=Oswald:wght@400;500;700&family=Source+Sans+3:wght@400&display=swap">
<style>
  :root {
    --page-bg: #ffffff;
    --banner-bg: #2f2631;
    --text-white: #ffffff;
    --accent-pink: #ff6aa8;
    --photo-warm: #b58a70;
    --photo-pink: #d9558f;
    --photo-blue: #554a8f;
  }
  * { margin: 0; padding: 0; box-sizing: border-box; }
  html, body {
    width: 1200px; height: 1000px;
    overflow: hidden;
    background: var(--page-bg);
  }
  .canvas { position: relative; width: 1200px; height: 1000px; }
  .banner {
    position: absolute; left: 264px; top: 227px;
    width: 672px; height: 584px; overflow: hidden;
    background: var(--banner-bg);
    color: var(--text-white);
  }
  .banner > * { position: absolute; line-height: 1; white-space: nowrap; }
  .headline-lead {
    left: 34px; top: 78px;
    font-family: "Jost", sans-serif; font-weight: 400;
    font-size: 34px; letter-spacing: 0;
  }
  .headline-accent {
    left: 34px; top: 116px;
    font-family: "Oswald", sans-serif; font-weight: 700;
    font-size: 52px; letter-spacing: 2.4px; color: var(--accent-pink);
  }
  .sale-lead {
    left: 35px; top: 199px;
    font-family: "Oswald", sans-serif; font-weight: 400;
    font-size: 37px; letter-spacing: 1.6px;
  }
  .sale-number {
    left: 38px; top: 242px;
    font-family: "Jost", sans-serif; font-weight: 400;
    font-size: 118px; letter-spacing: -3px;
  }
  .sale-percent {
    left: 167px; top: 250px;
    font-family: "Jost", sans-serif; font-weight: 400;
    font-size: 70px;
  }
  .sale-off {
    left: 168px; top: 305px;
    font-family: "Oswald", sans-serif; font-weight: 400;
    font-size: 37px; letter-spacing: 2.5px;
  }
  .shop-now {
    left: 45px; top: 369px;
    font-family: "Oswald", sans-serif; font-weight: 400;
    font-size: 25px; letter-spacing: 1.2px;
  }
  .shipping-note {
    left: 33px; top: 538px;
    font-family: "Source Sans 3", sans-serif; font-weight: 400;
    font-size: 22px;
  }
  .model-photo {
    left: 366px; top: 18px;
    width: 306px; height: 566px;
    border-radius: 140px 140px 0 0;
    background:
      radial-gradient(ellipse at 50% 18%, var(--photo-warm) 0%, rgba(181,138,112,0.5) 30%, rgba(181,138,112,0) 55%),
      linear-gradient(180deg, rgba(181,138,112,0.3) 0%, var(--photo-blue) 55%, var(--photo-pink) 100%);
  }
</style>
</head>
<body>
<main class="canvas">
  <section class="banner">
    <div class="model-photo" role="img" aria-label="Photo of a smiling model with long wavy hair wearing a fitted pink, blue and green watercolour-print dress, hands on hips"></div>
    <p class="headline-lead">NEW SEASON, NEW</p>
    <h1 class="headline-accent">SEXY DRESSES</h1>
    <p class="sale-lead">SALES UP TO</p>
    <p class="sale-number">60</p>
    <p class="sale-percent">%</p>
    <p class="sale-off">OFF</p>
    <p class="shop-now">SHOP NOW &gt;&gt;</p>
    <p class="shipping-note">"Free U.S shipping on orders $75+"</p>
  </section>
</main>
</body>
</html>
```